Commercial brochure presenting independent commercial activity

I would like to create a commercial brochure for my new professional activity.

This is a personal and not business oriented brochure because I will become an independent project assistant to assist engineering offices with one-off missions.

I want a 4 page A4 brochure

• Page 1: Logo, personal photo
• Page 2 and 3: Personal presentation and presentation of my activities
• Page4: contact information

My target audience: engineering offices and design offices

The objective of the brochure: it is to make my profile interesting so that design offices will want to use my services when there is demand

Sector of activity: food, chemical, pharmaceutical industry
The text of the brochure must remain in French and contain what is in the attached file

On page 1, you must keep a space for a photo of my profile which I will insert later because I do not have it yet and insert my monogram (it can be reworked to be inserted in the brochure)
The image with the logo (K/M) is the color range I want

engineering offices and design offices

industrie alimentaire, chimique, pharmaceutique

Sans Serif

0094D4
00A9DD
6FCCEA
C7EBF8
E9F6FB

• The plate must comply with current codes. Each reader must think that I am dynamic and that my services are of quality and equivalent to the presentation

```html
<!DOCTYPE html>
<html lang="fr">
<head>
<meta charset="utf-8">
<title>Karim Morel-Vuilloud – Brochure</title>
<link href="https://fonts.googleapis.com/css2?family=Poppins:wght@400;500;600;700&family=Roboto+Condensed:wght@400;600&family=Cormorant+Garamond:wght@500&display=swap" rel="stylesheet">
<style>
  :root{
    --blue:#0094D4;
    --blue-mid:#00A9DD;
    --blue-soft:#6FCCEA;
    --blue-pale:#C7EBF8;
    --blue-mist:#E9F6FB;
    --band:#d9ecf8;
    --ink:#1d1d1f;
    --label:#2b3266;
    --board:#d8d8d8;
    --white:#ffffff;
  }
  *{box-sizing:border-box;margin:0;padding:0}
  html,body{width:828px;height:1200px;overflow:hidden}
  body{background:var(--board);font-family:"Poppins",sans-serif;color:var(--ink);position:relative}
  .panel{position:absolute;width:334px;height:472px;background:var(--white);overflow:hidden}
  .spread{position:absolute;left:77px;width:668px;height:472px;box-shadow:3px 4px 8px rgba(0,0,0,.35)}
  .spread--cover{top:60px}
  .spread--inside{top:624px}
  .panel--left{left:0;top:0}
  .panel--right{left:334px;top:0}
  .board-label{position:absolute;font-family:"Poppins",sans-serif;font-weight:400;font-size:18px;color:var(--label);letter-spacing:.3px}

  /* back cover */
  .back__band{position:absolute;left:0;top:75px;width:334px;height:246px;background:linear-gradient(90deg,#1a87c6,var(--blue) 60%,#1b93d6)}
  .back__photo{position:absolute;left:29px;top:27px;width:281px;height:207px;border:2px solid var(--white);background:linear-gradient(160deg,#8fb86a 0%,#6f9a4e 35%,#b54a55 62%,#8a8f93 100%)}
  .wordmark{position:absolute;left:0;width:100%;text-align:center;font-family:"Cormorant Garamond",serif;font-weight:500;line-height:1;white-space:nowrap}
  .wordmark__name{font-size:14px;letter-spacing:.3px}
  .wordmark__role{font-size:6px;margin-top:2px;font-family:"Cormorant Garamond",serif}
  .back__mark{top:250px;color:var(--white)}
  .back__dot{position:absolute;left:151px;top:248px;width:32px;height:32px;border-radius:50%;border:2px solid var(--white)}
  .back__mark .wordmark__name{margin-top:38px}
  .contact{position:absolute;left:0;width:100%;text-align:center;font-weight:600;font-size:10px;color:#111;white-space:nowrap}
  .contact--address{top:351px}
  .contact--lines{top:369px;display:flex;justify-content:center;gap:18px}
  .contact__item{display:flex;align-items:center;gap:5px}
  .contact__rule{position:absolute;left:26px;top:388px;width:282px;height:2px;background:var(--blue)}

  /* front cover */
  .front__photo{position:absolute;inset:0;background:linear-gradient(180deg,#ffffff 0%,#f2f6f9 30%,#e3ebf0 60%,#cfd9df 100%)}
  .front__ring{position:absolute;left:85px;top:18px;width:38px;height:38px;border-radius:50%;border:2px solid var(--blue)}
  .front__mark{top:85px;left:8px;width:190px;color:var(--blue)}
  .front__mark .wordmark__name{font-size:17px}
  .front__mark .wordmark__role{font-size:7.5px}
  .front__bar{position:absolute;right:0;height:4px;background:var(--blue)}
  .front__bar--long{top:39px;width:59px}
  .front__bar--short{top:47px;width:30px;height:2.5px;background:var(--blue-soft)}

  /* inside */
  .head{position:absolute;left:0;top:10px;width:334px;height:44px;background:linear-gradient(90deg,#1a86c4,var(--blue));color:var(--white)}
  .head--left .head__title{position:absolute;left:21px;top:5px;font-family:"Roboto Condensed",sans-serif;font-weight:600;font-size:13.5px;letter-spacing:-.1px;line-height:1;white-space:nowrap}
  .head--left .head__sub{position:absolute;left:21px;top:21px;font-family:"Roboto Condensed",sans-serif;font-weight:400;font-size:12.5px;line-height:1;padding-bottom:3px;border-bottom:1px solid rgba(255,255,255,.5);white-space:nowrap}
  .head--right{height:43px}
  .head--right .head__title{position:absolute;left:18px;top:7px;font-weight:700;font-size:9.5px;line-height:1;padding-bottom:2px;border-bottom:1px solid rgba(255,255,255,.6)}
  .head--right .head__sub{position:absolute;left:18px;top:25px;font-weight:600;font-size:9.4px;line-height:1;white-space:nowrap}
  .intro{position:absolute;left:22px;top:62px;width:290px;font-size:5.6px;line-height:8.5px}
  .intro strong{font-weight:700}
  .band{position:absolute;left:0;width:334px;height:25px;background:var(--band)}
  .band__title{position:absolute;left:21px;top:7px;font-weight:700;font-size:9.2px;color:var(--blue);line-height:1;padding-bottom:1px;border-bottom:1px solid var(--blue-soft);white-space:nowrap}
  .item{position:absolute;font-size:9.3px;line-height:10px;padding-left:10px;white-space:nowrap}
  .item--wrap{white-space:normal}
  .item::before{content:"";position:absolute;left:0;top:2px;width:6.5px;height:6.5px;border-radius:50%;background:var(--blue)}
  .item::after{content:"";position:absolute;left:2px;top:3.6px;width:1.6px;height:3px;border:solid var(--white);border-width:0 1px 1px 0;transform:rotate(45deg)}
  .copy{position:absolute;left:18px;width:300px;font-size:9.4px;line-height:12px}
  .copy--atout{width:305px;line-height:12.4px;left:17px}
  .cta{position:absolute;left:0;width:334px;text-align:center;top:380px;font-size:8.3px;line-height:13.4px;color:var(--blue);font-weight:500;white-space:nowrap}
  .mini-mark{position:absolute;font-family:"Cormorant Garamond",serif;font-weight:500;font-size:8px;color:var(--blue);line-height:1;white-space:nowrap}
  .inside-rule{position:absolute;left:22px;top:461px;width:210px;height:1px;background:linear-gradient(90deg,var(--blue-pale),var(--blue))}
  .foot-strip{position:absolute;left:0;top:464px;width:334px;height:8px;background:var(--blue)}
</style>
</head>
<body>

<section class="spread spread--cover">
  <article class="panel panel--left back">
    <div class="back__band"></div>
    <div class="back__photo" role="img" aria-label="Photo de Karim Morel-Vuilloud en plein air, en montagne, dans son fauteuil tout-terrain"></div>
    <div class="back__dot"></div>
    <div class="wordmark back__mark">
      <div class="wordmark__name">Karim Morel-Vuilloud</div>
      <div class="wordmark__role">Assistant de projet indépendant</div>
    </div>
    <p class="contact contact--address">Ch. des Tilleuls 8 1870 Montval</p>
    <div class="contact contact--lines">
      <span class="contact__item">
        <svg width="9" height="9" viewBox="0 0 10 10" aria-hidden="true"><circle cx="5" cy="5" r="5" fill="#0094D4"/><path d="M3.2 2.6l1 1-.5.7c.4.8 1 1.4 1.8 1.8l.7-.5 1 1-.6.8C4.8 7.2 2.8 5.2 2.6 3.2z" fill="#fff"/></svg>
        +11 79 000 12 34
      </span>
      <span class="contact__item">
        <svg width="9" height="9" viewBox="0 0 10 10" aria-hidden="true"><circle cx="5" cy="5" r="5" fill="#0094D4"/><rect x="2.6" y="3.4" width="4.8" height="3.4" fill="none" stroke="#fff" stroke-width=".7"/><path d="M2.6 3.4L5 5.3l2.4-1.9" fill="none" stroke="#fff" stroke-width=".7"/></svg>
        karim@morel-vuilloud.ch
      </span>
    </div>
    <div class="contact__rule"></div>
  </article>

  <article class="panel panel--right front">
    <div class="front__photo" role="img" aria-label="Portrait professionnel d'un homme souriant en chemise blanche et cravate, dans un intérieur lumineux"></div>
    <div class="front__ring"></div>
    <div class="wordmark front__mark">
      <div class="wordmark__name">Karim Morel-Vuilloud</div>
      <div class="wordmark__role">Assistant de projet indépendant</div>
    </div>
    <div class="front__bar front__bar--long"></div>
    <div class="front__bar front__bar--short"></div>
  </article>
</section>

<p class="board-label" style="left:203px;top:558px">BACK</p>
<p class="board-label" style="left:570px;top:558px">FRONT</p>

<section class="spread spread--inside">
  <article class="panel panel--left">
    <header class="head head--left">
      <h1 class="head__title">KARIM MOREL-VUILLOUD :LOREM IPSUM</h1>
      <p class="head__sub">UN ATOUT PRÉCIEUX POUR VOTRE BUREAU D'ÉTUDES</p>
    </header>
    <p class="intro">Avec plus de 30 ans d'expérience dans l'industrie, je suis un expert chevronné en conception, gestion de projets et sécurité. J'offre mes services d'assistant de projet indépendant pour vous aider à gérer les pics de charge et les besoins spécifiques de votre bureau d'études.<br><strong>Mon expertise :</strong></p>

    <div class="band" style="top:96px"><h2 class="band__title">CONCEPTION &amp; DESIGN :</h2></div>
    <p class="item" style="left:21px;top:130px">Maquettes 3D (Tracéo Usine 3D)</p>
    <p class="item" style="left:21px;top:146px">Spécifications, catalogues,<br>définition des fournitures</p>
    <p class="item" style="left:197px;top:130px">Plans, schémas, RI/P&amp;ID,<br>Flowsheets</p>

    <div class="band" style="top:174px"><h2 class="band__title">GESTION DE PROJETS :</h2></div>
    <p class="item" style="left:21px;top:204px">Rédaction d'appels d'offre</p>
    <p class="item" style="left:21px;top:220px">Préparation de budgets</p>
    <p class="item" style="left:21px;top:236px">Réponse aux appels d'offre</p>
    <p class="item" style="left:172px;top:204px">Réalisation de plannings</p>
    <p class="item" style="left:172px;top:220px">Estimations budgétaires</p>

    <div class="band" style="top:250px"><h2 class="band__title">SÉCURITÉ :</h2></div>
    <p class="item" style="left:21px;top:282px">Sécurité machine</p>
    <p class="item" style="left:21px;top:298px">Edition de PHS</p>
    <p class="item" style="left:138px;top:282px">Plans de montage</p>

    <div class="band" style="top:314px"><h2 class="band__title">DOCUMENTATION TECHNIQUE :</h2></div>
    <p class="item" style="left:21px;top:349px">DESP</p>
    <p class="item" style="left:69px;top:349px">Documentations spécifiques</p>

    <div class="band" style="top:368px"><h2 class="band__title">EXPERTISE :</h2></div>
    <p class="item item--wrap" style="left:21px;top:399px;width:300px;line-height:11.2px">Ma connaissance approfondie de la métallurgie (tuyauterie, serrurerie, chaudronnerie, charpente métallique, montage) me permet de garantir des études complètes et d'éviter les oublis.</p>

    <div class="inside-rule"></div>
    <p class="mini-mark" style="left:240px;top:456px">Karim Morel-Vuilloud</p>
  </article>

  <article class="panel panel--right">
    <header class="head head--right">
      <h2 class="head__title">VOTRE AVANTAGE :</h2>
      <p class="head__sub">Connaissance des besoins des concepteurs et des fabricants :</p>
    </header>
    <p class="copy" style="top:63px">J'ai travaillé des deux côtés, ce qui me permet de comprendre les défis et les attentes de chacun</p>

    <div class="band" style="top:90px"><h2 class="band__title" style="left:18px">FLEXIBILITÉ :</h2></div>
    <p class="copy" style="top:123px">Je suis disponible pour des missions ponctuelles et à durée déterminée, sans engagement à long terme</p>

    <div class="band" style="top:149px"><h2 class="band__title" style="left:18px">EFFICACITÉ :</h2></div>
    <p class="copy" style="top:176px">Je peux vous aider à gérer les surcharges de travail et à respecter vos délais.</p>

    <div class="band" style="top:207px"><h2 class="band__title" style="left:18px">COLLABORATION FLUIDE :</h2></div>
    <p class="copy" style="top:239px">Je suis à votre disposition pour discuter de vos besoins et vous proposer des solutions sur mesure.</p>

    <div class="band" style="top:269px"><h2 class="band__title" style="left:18px">UN ATOUT UNIQUE :</h2></div>
    <p class="copy copy--atout" style="top:303px">Malgré mon handicap en fauteuil roulant, je suis totalement opérationnel et mon expérience me permet de vous offrir une expertise de haut niveau. Je suis disponible à 35% dès septembre 2024 et je suis prêt à mettre mon expertise et mon dynamisme au service de votre succès</p>

    <p class="cta">N'HÉSITEZ PAS À ME CONTACTER POUR DISCUTER DE VOS BESOINS<br>ET DÉCOUVRIR COMMENT JE PEUX VOUS AIDER À ATTEINDRE<br>VOS OBJECTIFS.</p>

    <p class="mini-mark" style="left:244px;top:440px">Karim Morel-Vuilloud</p>
    <div class="foot-strip"></div>
  </article>
</section>

<p class="board-label" style="left:386px;top:1138px">INSIDE</p>

</body>
</html>
```